Bright Path Therapies business cards and stationary

Need business cards and stationary designed to match previously made logo for for a new company based in Sydney NSW called 'Bright Path Therapies'.

We provide early intervention services and diagnostic assessment for children with disability and their families. I would like designs that are colourful and child friendly - possibly using feet/footprints/steps on a white background. The final design should communicate that we are family friendly, accepting and fun to work with.

Target Market(s)

Parents and Families
Teachers
Allied Health Professionals

Industry/Entity Type

Psychology

Contact Information for Business Card

Bright Path Therapies
www.brightpaththerapies.example
info@brightpaththerapies.example

Font styles to use
Sans Serif
Decorative
Script

Requirements
Must have
• Match the font and colour scheme of logo, along with footprint picture
Nice to have
• Clean and simple, while reflecting that I am working with families.
• Also- editable for when we make staff specific cards.

```html
<!DOCTYPE html>
<html lang="en">
<head>
<meta charset="utf-8">
<title>Bright Path Therapies — Business Cards</title>
<link rel="stylesheet" href="https://fonts.googleapis.com/css2?family=Amatic+SC:wght@700&display=swap">
<style>
  :root {
    --stage: #3a3a3a;
    --brand-red: #ef4136;
    --brand-red-tint: #f0564c;
    --card-white: #ffffff;
    --print-tint: #fdf1f0;
    --brand-blue: #1f6fb8;
    --ink-white: #ffffff;
  }
  * { box-sizing: border-box; margin: 0; padding: 0; }
  html, body {
    width: 1200px;
    height: 771px;
    overflow: hidden;
    background: var(--stage);
  }
  .stage {
    position: relative;
    width: 1200px;
    height: 771px;
    display: flex;
    align-items: center;
    justify-content: center;
    gap: 60px;
  }
  .card {
    position: relative;
    width: 510px;
    height: 294px;
    border-radius: 3px;
    overflow: hidden;
    font-family: "Amatic SC", "Arial Narrow", sans-serif;
    font-weight: 700;
  }
  .card--front { background: var(--brand-red); }
  .card--back { background: var(--card-white); }
  .card__pattern {
    position: absolute;
    inset: 0;
  }
  .card--front .card__pattern { background: linear-gradient(135deg, var(--brand-red-tint), var(--brand-red)); }
  .card--back .card__pattern { background: linear-gradient(135deg, var(--print-tint), var(--card-white)); }
  .card__content {
    position: relative;
    height: 100%;
    display: flex;
    flex-direction: column;
    justify-content: center;
    padding: 0 44px;
    gap: 14px;
  }
  .brand {
    display: flex;
    align-items: center;
    gap: 18px;
  }
  .brand__dot {
    flex: none;
    width: 82px;
    height: 82px;
    border-radius: 50%;
  }
  .brand__name {
    font-size: 50px;
    line-height: 1;
    letter-spacing: 1px;
  }
  .card--front .brand__dot { background: var(--ink-white); }
  .card--front .brand__name { color: var(--ink-white); }
  .card--back .brand__dot { background: var(--brand-red); }
  .card--back .brand__name { color: var(--brand-blue); }
  .contact {
    font-size: 27px;
    letter-spacing: 1.5px;
    padding-left: 4px;
  }
  .card--front .contact { color: var(--ink-white); }
  .card--back .contact { color: var(--brand-red); }
</style>
</head>
<body>
  <main class="stage">
    <section class="card card--front">
      <div class="card__pattern" role="img" aria-label="Faint repeating footprint pattern in lighter red"></div>
      <div class="card__content">
        <div class="brand">
          <span class="brand__dot"></span>
          <span class="brand__name">Bright Path Therapies</span>
        </div>
        <p class="contact">www.brightpaththerapies.example</p>
      </div>
    </section>
    <section class="card card--back">
      <div class="card__pattern" role="img" aria-label="Faint repeating footprint pattern in pale pink"></div>
      <div class="card__content">
        <div class="brand">
          <span class="brand__dot"></span>
          <span class="brand__name">Bright Path Therapies</span>
        </div>
        <p class="contact">info@brightpaththerapies.example</p>
      </div>
    </section>
  </main>
</body>
</html>
```